GLS biz card

We need a business card design for our new company based in Los Angeles called "Gold Lantern Studios". We develop film and television projects. We work with investors, financiers, film production companies, film distribution and sales companies as well as studios. We would like to incorporate our logo (see attached) on a two-sided card. We need to include: name and title, address, phone, email and company website.

Target Market(s)

Business, financial and studio clients

Industry/Entity Type

Business

Contact Information for Business Card

Two-sided. We are thinking of the logo on one side and the information on the back. Please feel free to be creative! Thanks.

Requirements
Must have
• Please include the following text information, excluding the "CAPS CATEGORY:" and please allow the ability for us to change the name, title and email address for each company employee):
• NAME & TITLE:
• Peter Dunmore
• Managing Partner
• COMPANY NAME:
• GOLD LANTERN STUDIOS (please use existing logo)
• COMPANY ADDRESS:
• KVT Arts Park
• 2480 Wexley Boulevard
• Arts Hall, 4th Floor
• Manhattan Beach, CA 90266
• COMPANY PHONE NUMBER:
• 310-555-4206
• COMPANY WEBSITE ADDRESS:
• www.goldlanternstudioshouse.com
• EMAIL ADDRESS: (only one per card)
• frank@goldlanternstudioshouse.com
• tizzy@goldlanternstudioshouse.com
• peter@goldlanternstudioshouse.com

```html
<!DOCTYPE html>
<html lang="en">
<head>
<meta charset="utf-8">
<title>Gold Lantern Studios – Business Card</title>
<link href="https://fonts.googleapis.com/css2?family=PT+Sans+Narrow:wght@400;700&display=swap" rel="stylesheet">
<style>
  :root {
    --page: #2b2b2b;
    --card: #050505;
    --accent: #1fa9d9;
    --accent-light: #7fd3f0;
    --band-mid: #eef6fa;
    --text: #e8e8e8;
    --muted: #cfcfcf;
  }
  * { margin: 0; padding: 0; box-sizing: border-box; }
  html, body {
    width: 1200px; height: 900px; overflow: hidden;
    background: var(--page);
    font-family: "PT Sans Narrow", sans-serif;
  }
  .sheet {
    width: 1200px; height: 900px;
    display: flex; flex-direction: column;
    align-items: center; justify-content: center; gap: 24px;
  }
  .card {
    position: relative;
    width: 700px; height: 400px;
    background: var(--card);
    border-radius: 16px;
    overflow: hidden;
    box-shadow: 0 10px 30px rgba(0,0,0,.55);
  }

  /* Info side */
  .brand-lockup {
    position: absolute; left: 60px; top: 110px;
    width: 260px;
    display: flex; flex-direction: column; align-items: center; gap: 18px;
  }
  .brand-dot {
    width: 96px; height: 96px; border-radius: 50%;
    background: var(--accent);
  }
  .brand-name {
    color: var(--accent);
    font-weight: 700; font-size: 28px; letter-spacing: 2px;
    text-align: center; line-height: 1.1;
  }
  .contact {
    position: absolute; left: 370px; top: 34px;
    color: var(--text);
  }
  .person-name {
    color: var(--accent);
    font-weight: 700; font-size: 30px; letter-spacing: .5px;
  }
  .person-title { font-size: 18px; margin-top: 2px; }
  .details { list-style: none; margin-top: 24px; font-size: 17px; }
  .details li { display: flex; align-items: center; gap: 8px; line-height: 26px; }
  .details svg { width: 16px; height: 16px; fill: var(--accent); flex: none; }
  .address { margin-top: 22px; font-size: 17px; line-height: 24px; color: var(--muted); padding-left: 2px; }
  .band {
    position: absolute; left: 0; right: 0; bottom: 36px; height: 14px;
    background: linear-gradient(90deg, var(--accent) 0%, var(--accent-light) 30%, var(--band-mid) 50%, var(--accent-light) 70%, var(--accent) 100%);
  }

  /* Logo side */
  .card--front {
    display: flex; flex-direction: column; align-items: center; justify-content: center; gap: 26px;
  }
  .card--front .brand-dot { width: 140px; height: 140px; }
  .card--front .brand-name { font-size: 44px; letter-spacing: 3px; }
</style>
</head>
<body>
<main class="sheet">
  <section class="card card--back" aria-label="Card back with contact details">
    <div class="brand-lockup">
      <div class="brand-dot"></div>
      <div class="brand-name">GOLD LANTERN STUDIOS</div>
    </div>
    <div class="contact">
      <h1 class="person-name">PETER DUNMORE</h1>
      <p class="person-title">Managing Partner</p>
      <ul class="details">
        <li>
          <svg viewBox="0 0 24 24" aria-hidden="true"><path d="M6.6 10.8a15.1 15.1 0 0 0 6.6 6.6l2.2-2.2c.3-.3.7-.4 1-.2 1.1.4 2.3.6 3.6.6.6 0 1 .4 1 1V20c0 .6-.4 1-1 1A17 17 0 0 1 3 4c0-.6.4-1 1-1h3.5c.6 0 1 .4 1 1 0 1.3.2 2.5.6 3.6.1.3 0 .7-.2 1z"/></svg>
          310-555-4206
        </li>
        <li>
          <svg viewBox="0 0 24 24" aria-hidden="true"><path d="M2 5h20v14H2z M3.5 6.5 12 13l8.5-6.5" stroke="#050505" stroke-width="1.5"/></svg>
          peter@goldlanternstudioshouse.com
        </li>
        <li>
          <svg viewBox="0 0 24 24" aria-hidden="true"><circle cx="12" cy="12" r="10"/><path d="M2 12h20M12 2c3 3 3 17 0 20M12 2c-3 3-3 17 0 20" stroke="#050505" stroke-width="1.3" fill="none"/></svg>
          www.goldlanternstudioshouse.com
        </li>
      </ul>
      <p class="address">
        KVT Arts Park<br>
        2480 Wexley Boulevard Arts Hall,<br>
        4th Floor Manhattan Beach, CA 90266
      </p>
    </div>
    <div class="band"></div>
  </section>

  <section class="card card--front" aria-label="Card front with company name">
    <div class="brand-dot"></div>
    <div class="brand-name">GOLD LANTERN STUDIOS</div>
  </section>
</main>
</body>
</html>
```